Lumora Education - new College Consulting company in San Francisco needs a flyer design

We need a logo design for a new college admissions consulting business in San Francisco Bay Area and San Jose called 'Lumora Education'. We plan to develop tailor-made strategies for each students dreams and aspirations and will help provide them with online classes and in-person consulting starting Summer 2022.
Lumora Education plans on providing a free first time consulting to attract clients and grow our client base from there.
Lumora Education has a small team of consultants who have degrees from Economics/Business, Biology, and Computer Science who can provide tailored guidance to meet student and parent expectations and spend the time to walk them throughout the process.
Please refer to attached logos for the company and to create a flyer.
Target Market(s)
Competitive College Consulting
Industry/Entity Type
Education Consulting
Look and feel

```html
<!DOCTYPE html>
<html lang="en">
<head>
<meta charset="utf-8">
<title>Lumora Education Flyer</title>
<link href="https://fonts.googleapis.com/css2?family=Bebas+Neue&family=Archivo+Black&family=Poppins:wght@400;500;600;700&family=Lora:wght@400&display=swap" rel="stylesheet">
<style>
  :root {
    --coral: #f8948b;
    --coral-text: #f4867c;
    --ink: #1f1f1f;
    --band: #2a2a2a;
    --white: #ffffff;
    --blue: #1f7fc4;
    --page: #f2f2f2;
  }
  * { box-sizing: border-box; margin: 0; padding: 0; }
  html, body { width: 707px; height: 1200px; overflow: hidden; background: var(--page); }
  .stage { position: relative; width: 707px; height: 1200px; }
  .flyer {
    position: absolute; left: 0; top: 142px;
    width: 765px; height: 990px;
    transform: scale(0.924); transform-origin: top left;
    background: var(--white); overflow: hidden;
    font-family: "Poppins", sans-serif; color: var(--ink);
  }
  .abs { position: absolute; }

  /* Hero */
  .hero { left: 0; top: 0; width: 765px; height: 397px; background: var(--coral); }
  .hero-photo {
    left: 380px; top: 0; width: 385px; height: 397px;
    background: linear-gradient(90deg, rgba(248,148,139,0) 0%, #d98c84 25%, #b9857d 55%, #8e6c6a 100%);
  }
  .brand { right: 462px; top: 46px; text-align: right; white-space: nowrap; }
  .brand-name { font-family: "Poppins", sans-serif; font-weight: 500; font-size: 20px; color: var(--ink); line-height: 1.1; }
  .brand-tagline { font-family: "Lora", serif; font-size: 18px; color: var(--ink); margin-top: 2px; }
  .brand-mark { left: 318px; top: 52px; width: 40px; height: 40px; border-radius: 50%; background: var(--ink); }
  .title { left: 50px; font-family: "Bebas Neue", sans-serif; font-size: 94px; line-height: 1; letter-spacing: 0.5px; }
  .title-top { top: 128px; color: var(--ink); }
  .title-edu { top: 207px; color: var(--white); }
  .tag-bar { left: 52px; top: 312px; width: 3px; height: 58px; background: var(--ink); }
  .tagline { left: 71px; top: 310px; font-size: 18.5px; font-weight: 600; line-height: 22px; }

  /* Offer band */
  .band { left: 0; top: 397px; width: 765px; height: 38px; background: var(--band); }
  .band-text { left: 54px; top: 405px; font-size: 16px; font-weight: 500; color: var(--white); }
  .free-shape { left: 0; top: 410px; }
  .free-word { left: 535px; top: 428px; font-family: "Archivo Black", sans-serif; font-size: 66px; line-height: 1; color: var(--ink); }
  .free-sub { left: 536px; top: 490px; font-family: "Bebas Neue", sans-serif; font-size: 28px; color: var(--white); line-height: 1; }
  .service-icon { width: 58px; height: 58px; top: 457px; background: var(--coral); border-radius: 5px; }
  .service-label { top: 466px; font-size: 16.5px; font-weight: 500; line-height: 20px; }
  .service-divider { left: 220px; top: 455px; width: 2px; height: 62px; background: #dddddd; }

  /* Team */
  .team { left: 0; top: 535px; width: 765px; height: 237px; background: var(--ink); }
  .team-photo {
    left: 430px; top: 535px; width: 335px; height: 237px;
    background: linear-gradient(90deg, #1f1f1f 0%, #4a4644 25%, #77706c 60%, #a9a4a1 100%);
  }
  .team-intro { left: 52px; top: 546px; font-size: 18.5px; color: var(--white); line-height: 22px; }
  .subject { font-size: 24px; font-weight: 500; color: var(--coral-text); line-height: 30px; }
  .star { color: var(--white); font-size: 20px; margin-right: 6px; }
  .team-rule { left: 52px; top: 690px; width: 345px; height: 1px; background: #8a8a8a; }
  .team-note { left: 52px; top: 704px; font-size: 14px; color: var(--white); line-height: 17px; }

  /* Facts */
  .body-copy { left: 54px; top: 793px; font-size: 13.8px; line-height: 17px; }
  .facts-rule { left: 390px; top: 798px; width: 2px; height: 115px; background: #cfcfcf; }
  .facts-title { left: 413px; top: 790px; font-size: 24px; font-weight: 500; color: var(--coral-text); }
  .facts-lead { left: 415px; top: 824px; font-size: 14px; line-height: 17px; }
  .facts-rate { left: 415px; font-size: 16px; }
  .facts-rate b { color: var(--blue); font-weight: 600; }

  /* Footer */
  .foot-call { left: 0; top: 930px; width: 392px; height: 60px; background: var(--coral); }
  .foot-web { left: 392px; top: 930px; width: 373px; height: 60px; background: var(--ink); }
  .call-text { left: 54px; top: 939px; font-size: 29px; font-weight: 700; color: var(--ink); }
  .web-text { left: 417px; top: 942px; font-size: 23px; font-weight: 600; color: var(--coral-text); }
</style>
</head>
<body>
<div class="stage">
  <div class="flyer">
    <div class="abs hero"></div>
    <div class="abs hero-photo" role="img" aria-label="Three smiling students holding books in front of a classical university building"></div>

    <div class="abs brand">
      <div class="brand-name">Lumora Education</div>
      <div class="brand-tagline">Learning is a phenomenom</div>
    </div>
    <div class="abs brand-mark"></div>

    <div class="abs title title-top">LUMORA</div>
    <div class="abs title title-edu">EDUCATION</div>
    <div class="abs tag-bar"></div>
    <div class="abs tagline">We plan to develop tailor-made<br>strategies for each students<br>dreams and aspirations.</div>

    <div class="abs band"></div>
    <div class="abs band-text">Starting Summer&nbsp; 2022 We will help provide them with</div>

    <svg class="abs free-shape" width="765" height="125" viewBox="0 0 765 125">
      <polygon points="520,0 765,0 765,125 465,125" fill="var(--coral)"/>
    </svg>
    <div class="abs free-word">FREE</div>
    <div class="abs free-sub">FIRST TIME CONSULTING</div>

    <div class="abs service-icon" style="left:52px">
      <svg width="58" height="58" viewBox="0 0 58 58" fill="none" stroke="#fff" stroke-width="2.2" stroke-linejoin="round">
        <rect x="16" y="17" width="26" height="18" rx="2"/>
        <path d="M12 39 H46 L43 42 H15 Z"/>
        <circle cx="29" cy="24" r="3"/>
        <path d="M23 33 Q29 27 35 33"/>
      </svg>
    </div>
    <div class="abs service-label" style="left:126px">Online<br>Classes</div>
    <div class="abs service-divider"></div>
    <div class="abs service-icon" style="left:250px">
      <svg width="58" height="58" viewBox="0 0 58 58" fill="none" stroke="#fff" stroke-width="2.2" stroke-linejoin="round">
        <rect x="24" y="12" width="16" height="10" rx="2"/>
        <path d="M28 22 L27 26 L32 22"/>
        <circle cx="22" cy="30" r="3.5"/>
        <path d="M15 44 V38 Q22 33 29 38 V44"/>
        <path d="M12 44 H46"/>
      </svg>
    </div>
    <div class="abs service-label" style="left:320px">In-person<br>Consulting</div>

    <div class="abs team"></div>
    <div class="abs team-photo" role="img" aria-label="Graduate in cap and gown with a parent and a consultant in a university hall"></div>
    <div class="abs team-intro">Lumora Education has a small team of<br>consultants who have degrees from</div>
    <div class="abs subject" style="left:52px;top:604px"><span class="star">★</span>Economics</div>
    <div class="abs subject" style="left:52px;top:641px"><span class="star">★</span>Biology</div>
    <div class="abs subject" style="left:245px;top:604px"><span class="star">★</span>Computer<br><span style="padding-left:25px">Science</span></div>
    <div class="abs team-rule"></div>
    <div class="abs team-note">Who can provide tailored guidance to meet<br>student and parent expectations and spend<br>the time to walk them throughout the process.</div>

    <div class="abs body-copy">Lorem Ipsum is simply dummy text of the<br>printing and typesetting industry.<br>Lorem Ipsum has been the industry's<br>standard dummy text ever since the 1500s,<br>when an unknown printer took a galley of<br>type and scrambled it to make a<br>type specimen book.</div>
    <div class="abs facts-rule"></div>
    <div class="abs facts-title">Admission Facts and tips</div>
    <div class="abs facts-lead">In the last 9 years, the average college<br>admission ratres has dropped by 49%</div>
    <div class="abs facts-rate" style="top:866px">Admission Rate in <b>2005- 17.1%</b></div>
    <div class="abs facts-rate" style="top:891px">Admission Rate in <b>2015- 9.9%</b></div>

    <div class="abs foot-call"></div>
    <div class="abs foot-web"></div>
    <div class="abs call-text">Call US: 0198-765-432</div>
    <div class="abs web-text">www.lumoraeducation.com</div>
  </div>
</div>
</body>
</html>
```